Tidalux Globalwear Co. Shopify (Rebrand)

FULL WEBSITE AUDIT AND REBRAND
CLEAN Simplistic LOOK
Little Friction, Functional
COLORS: BLUE,ORANGE,BLACK, WHITE.
I upload a google doc with further information and social media sites to get a better understanding a design concept.
NEW WEBISTE LINK: www.tidaluxglobalwear.example

Front page photos

Consistent photography
Good product descriptions
How we started brand story 🎯
Brand ascetic🎯
Home page call to Action
***OUR TIDALUX***
this will highlight brand story and customer photos and reviews
Great Clothing Brand Websites I take inspiration from for website

https://www.qvbrtlso.example

https://plantcedarvillages.example

https://oftenkinpalo.example

https://tidepikez.example/?fbclid=XQRtuvwMNB4hPlzKeC71sTyoWqVbHn2cGdf5rJml8pxoUZEYHk3NdQsBfZgXy
Setup for easy accessibility of photography with new collections.

```html
<!DOCTYPE html>
<html lang="en">
<head>
<meta charset="utf-8">
<title>Tidalux Globalwear Co. — Home</title>
<link rel="stylesheet" href="https://fonts.googleapis.com/css2?family=Audiowide&family=Poppins:wght@300;400;500;600&display=swap">
<style>
:root{
  --orange:#f47b34;
  --blue:#2f6db3;
  --ink:#1b1b1b;
  --white:#ffffff;
  --muted:#6d6d6d;
  --footer:#1d1d1d;
  --line:#d9d9d9;
}
*{box-sizing:border-box;margin:0;padding:0}
html,body{width:1200px;height:4988px;overflow:hidden}
body{position:relative;background:var(--white);font-family:'Poppins',sans-serif;color:var(--ink)}
.abs{position:absolute}
.display{font-family:'Audiowide',sans-serif;text-transform:uppercase}

.promo-bar{left:0;top:0;width:1200px;height:35px;background:var(--orange);color:var(--white);font-size:11px;letter-spacing:1.5px;display:flex;align-items:center;justify-content:center}
.site-header{left:0;top:35px;width:1200px;height:81px}
.brand{left:101px;top:46px;height:62px;display:flex;align-items:center;gap:12px;font-size:20px;font-weight:600;color:var(--blue);letter-spacing:.5px}
.brand-dot{width:52px;height:52px;border-radius:50%;background:var(--orange)}
.main-nav{top:68px;font-size:13px;font-weight:500;letter-spacing:.3px}
.main-nav.active{color:var(--orange)}
.main-nav.active::after{content:"";position:absolute;left:0;right:0;top:24px;height:2px;background:var(--orange)}
.header-icon{top:64px}

.photo{display:block}
.hero{left:0;top:116px;width:1200px;height:624px;background:linear-gradient(180deg,#c9d3d6 0%,#7f9a73 45%,#4d6a3e 100%)}
.hero-title{left:101px;top:346px;color:var(--white);font-size:29px;line-height:34px;letter-spacing:1px}
.btn{background:var(--orange);color:var(--white);font-size:13px;font-weight:600;border-radius:20px;display:flex;align-items:center;justify-content:center;text-transform:uppercase}
.hero-btn{left:99px;top:441px;width:155px;height:37px}
.hero-dots{left:559px;top:700px;display:flex;gap:14px}
.hero-dots span{width:12px;height:12px;border-radius:50%;border:1.5px solid var(--white)}
.hero-dots span.on{background:var(--white)}

.eyebrow{left:0;width:1200px;text-align:center;color:var(--orange);font-size:12px;letter-spacing:3px;display:flex;justify-content:center;align-items:center;gap:10px}
.eyebrow::before,.eyebrow::after{content:"";width:24px;height:1px;background:var(--orange)}
.section-title{left:0;width:1200px;text-align:center;font-size:38px;letter-spacing:1px}

.card-img{overflow:hidden;width:319px;height:393px}
.ribbon{position:absolute;left:-38px;top:24px;width:150px;height:22px;background:var(--orange);color:var(--white);font-size:10px;text-align:center;line-height:22px;transform:rotate(-45deg)}
.card-name{width:319px;text-align:center;font-size:17px}
.card-price{width:319px;text-align:center;font-size:16px}
.arrow{width:24px;height:40px}

.tile{top:1444px;height:531px}
.tile-label{width:100%;text-align:center;color:var(--white);font-size:38px;letter-spacing:2px}

.banner{left:0;top:1996px;width:1200px;height:531px;background:linear-gradient(180deg,#b7c7cf 0%,#5a6d4a 45%,#2b2e2b 100%)}
.banner-title{left:0;top:2303px;width:1200px;text-align:center;color:var(--white);font-size:32px;line-height:41px;font-style:italic}
.banner-btn{left:523px;top:2408px;width:155px;height:39px}

.story-band{left:0;top:3231px;width:1200px;height:531px;background:linear-gradient(90deg,#6f8f66 0%,#c8d2d4 45%,#a9b89c 75%,#5e7a4d 100%)}
.story-card{left:635px;top:3305px;width:466px;height:383px;background:var(--white);box-shadow:0 4px 18px rgba(0,0,0,.15);padding:50px 30px 0 29px}
.story-card h2{font-size:36px;font-weight:400;margin-bottom:14px}
.story-card p{font-size:12.4px;line-height:26.2px;color:#444;text-align:justify}

.gram{width:236px;height:240px}

.perk{top:4530px;display:flex;align-items:center;gap:13px}
.perk-icon{width:50px;height:50px;border-radius:50%;border:1.5px solid #9a9a9a;display:flex;align-items:center;justify-content:center}
.perk h4{font-size:12.5px;font-weight:600}
.perk p{font-size:10.5px;color:var(--muted)}

.site-footer{left:0;top:4629px;width:1200px;height:359px;background:var(--footer);color:var(--white)}
.foot-head{top:4688px;font-size:12.5px;font-weight:600;letter-spacing:.5px}
.foot-list{top:4719px;font-size:11.5px;line-height:26px;list-style:none;color:#e2e2e2}
.newsletter{left:101px;top:4719px;width:210px;height:26px;border-bottom:1px solid var(--white);font-size:11.5px;color:#e2e2e2}
.social{top:4765px;width:35px;height:35px;border-radius:50%;border:1.5px solid var(--white)}
.foot-brand{left:886px;top:4689px;display:flex;align-items:center;gap:10px;font-size:16px;font-weight:600;color:var(--white)}
.foot-brand-dot{width:44px;height:44px;border-radius:50%;background:var(--white)}
.store-link{left:892px;top:4758px;font-size:12px;font-weight:600;display:flex;gap:5px;align-items:center}
.pay{top:4795px;width:44px;height:27px;border-radius:3px}
.copyright{left:0;top:4952px;width:1200px;text-align:center;font-size:11.5px;color:#cfcfcf}
</style>
</head>
<body>

<div class="abs promo-bar">🎁 DREAMS IN MOTION.USE CODE: TIDAL10 FOR 10% OFF</div>

<header class="abs site-header"></header>
<div class="abs brand"><span class="brand-dot"></span>Tidalux Globalwear Co.</div>
<span class="abs main-nav active" style="left:437px">HOME</span>
<span class="abs main-nav" style="left:513px">ABOUT US</span>
<span class="abs main-nav" style="left:617px">T-SHIRTS</span>
<span class="abs main-nav" style="left:716px">HOODIES</span>
<span class="abs main-nav" style="left:813px">BLOG</span>
<span class="abs main-nav" style="left:885px">CONTACT US</span>
<svg class="abs header-icon" style="left:1011px" width="20" height="22" viewBox="0 0 20 22" fill="none" stroke="#222" stroke-width="1.6"><circle cx="10" cy="7" r="5"/><path d="M2 21c0-5 4-8 8-8s8 3 8 8"/></svg>
<svg class="abs header-icon" style="left:1042px" width="20" height="22" viewBox="0 0 20 22" fill="none" stroke="#222" stroke-width="1.8"><circle cx="8" cy="9" r="6.5"/><path d="M13 14l6 6"/></svg>
<svg class="abs header-icon" style="left:1072px" width="26" height="22" viewBox="0 0 26 22" fill="none" stroke="#222" stroke-width="1.6"><path d="M2 8h20l-2.5 12h-15z"/><path d="M7 8l4-6M17 8l-4-6"/><circle cx="21" cy="5" r="4" fill="var(--orange)" stroke="none"/></svg>

<div class="abs hero photo" role="img" aria-label="Two models in black hoodies walking across a park lawn"></div>
<h1 class="abs hero-title display">Dreams don't work<br>unless you do</h1>
<a class="abs btn hero-btn">Shop now</a>
<svg class="abs arrow" style="left:62px;top:406px" viewBox="0 0 24 40" fill="none" stroke="#fff" stroke-width="1.5"><path d="M18 4L4 20l14 16"/></svg>
<svg class="abs arrow" style="left:1114px;top:406px" viewBox="0 0 24 40" fill="none" stroke="#fff" stroke-width="1.5"><path d="M6 4l14 16L6 36"/></svg>
<div class="abs hero-dots"><span></span><span class="on"></span><span></span><span></span></div>

<div class="abs eyebrow" style="top:819px">OUT OF THIS WORLD</div>
<h2 class="abs section-title display" style="top:842px">Featured Products</h2>
<svg class="abs arrow" style="left:60px;top:1084px" viewBox="0 0 24 40" fill="none" stroke="#222" stroke-width="1.6"><path d="M18 4L4 20l14 16"/></svg>
<svg class="abs arrow" style="left:1114px;top:1084px" viewBox="0 0 24 40" fill="none" stroke="#222" stroke-width="1.6"><path d="M6 4l14 16L6 36"/></svg>
<div class="abs card-img photo" style="left:101px;top:906px;background:linear-gradient(180deg,#5d7a3c,#2f3f26)" role="img" aria-label="Model wearing a black graphic tee among green foliage"></div>
<div class="abs card-img photo" style="left:440px;top:906px;background:linear-gradient(180deg,#6b3a2a,#2a1d18)" role="img" aria-label="Model in a black tee with a red chest print"><span class="ribbon">30% OFF</span></div>
<div class="abs card-img photo" style="left:780px;top:906px;background:linear-gradient(180deg,#8fb07a,#d8dcd4)" role="img" aria-label="Model in a white tee with a green chest print"></div>
<div class="abs card-name" style="left:101px;top:1310px">Tidalux To The Moon Tee</div>
<div class="abs card-name" style="left:440px;top:1310px">Tidalux To The Moon Tee</div>
<div class="abs card-name" style="left:780px;top:1310px">Tidalux To The Moon Tee</div>
<div class="abs card-price" style="left:101px;top:1340px">$19.99 USD</div>
<div class="abs card-price" style="left:440px;top:1340px">$19.99 USD</div>
<div class="abs card-price" style="left:780px;top:1340px">$19.99 USD</div>

<div class="abs tile photo" style="left:0;width:587px;background:linear-gradient(180deg,#3f5a2c,#1f2a1a)" role="img" aria-label="Model crouching in a black graphic tee before a hedge"></div>
<div class="abs tile photo" style="left:612px;width:588px;background:linear-gradient(180deg,#c3ccc9,#4f5a4c 60%,#2a2d2b)" role="img" aria-label="Model seated on a ledge in a black hoodie"></div>
<div class="abs tile-label display" style="left:0;top:1893px;width:587px">T-shirts</div>
<div class="abs tile-label display" style="left:612px;top:1893px;width:588px">Hoodies</div>

<div class="abs banner photo" role="img" aria-label="Three models in black hoodies standing together outdoors"></div>
<h2 class="abs banner-title display">The standard lorem ipsum pe,<br>used since the 1500s</h2>
<a class="abs btn banner-btn">Shop now</a>

<div class="abs eyebrow" style="top:2606px">OUT OF THIS WORLD</div>
<h2 class="abs section-title display" style="top:2629px">Best Seller</h2>
<svg class="abs arrow" style="left:60px;top:2870px" viewBox="0 0 24 40" fill="none" stroke="#222" stroke-width="1.6"><path d="M18 4L4 20l14 16"/></svg>
<svg class="abs arrow" style="left:1114px;top:2870px" viewBox="0 0 24 40" fill="none" stroke="#222" stroke-width="1.6"><path d="M6 4l14 16L6 36"/></svg>
<div class="abs card-img photo" style="left:101px;top:2693px;background:linear-gradient(180deg,#7d8f73,#2c2c2c)" role="img" aria-label="Back view of a black hoodie with script print by the water"></div>
<div class="abs card-img photo" style="left:440px;top:2693px;background:linear-gradient(180deg,#e6e6e6,#2a2a2a 55%,#555)" role="img" aria-label="Back view of a black hoodie with space graphic"><span class="ribbon">30% OFF</span></div>
<div class="abs card-img photo" style="left:780px;top:2693px;background:linear-gradient(180deg,#a9c0d8,#5a6f8a 60%,#2f4a7a)" role="img" aria-label="Model in a grey jacket in front of a painted mural"></div>
<div class="abs card-name" style="left:101px;top:3097px">Tidalux To The Moon Tee</div>
<div class="abs card-name" style="left:440px;top:3097px">Tidalux To The Moon Tee</div>
<div class="abs card-name" style="left:780px;top:3097px">Tidalux To The Moon Tee</div>
<div class="abs card-price" style="left:101px;top:3127px">$19.99 USD</div>
<div class="abs card-price" style="left:440px;top:3127px">$19.99 USD</div>
<div class="abs card-price" style="left:780px;top:3127px">$19.99 USD</div>

<div class="abs story-band photo" role="img" aria-label="Two models in white and black tees standing outdoors"></div>
<article class="abs story-card">
  <h2 class="display">Our Story</h2>
  <p>TIDALUX started a concept in my childhood of making it out of poverty and creating opportunities through work ethic and vision which came from the space theme. I would plan with patience how I would take the next steps toward my future. Battling the pitfalls of my surroundings while also tryna stay in line mentally. Many losses in this process. The concept was to live a life of abundance that has been earned through hard work ethic.</p>
</article>

<div class="abs eyebrow" style="top:3839px">FOLLOW US</div>
<h2 class="abs section-title display" style="top:3864px">On Snapgrid</h2>
<div class="abs gram photo" style="left:101px;top:3938px;background:linear-gradient(180deg,#c6d3da,#6f8560)" role="img" aria-label="Model posing by palm trees"></div>
<div class="abs gram photo" style="left:354px;top:3938px;background:linear-gradient(180deg,#d9dde0,#2b2b2b)" role="img" aria-label="Seated model showing hoodie back print"></div>
<div class="abs gram photo" style="left:608px;top:3938px;background:linear-gradient(180deg,#7b8a6a,#2c2c2c)" role="img" aria-label="Model in black hoodie seated outdoors"></div>
<div class="abs gram photo" style="left:862px;top:3938px;background:linear-gradient(180deg,#b9c6cb,#4e6340)" role="img" aria-label="Two models walking in the park"></div>
<div class="abs gram photo" style="left:101px;top:4195px;background:linear-gradient(180deg,#4a6b33,#2a2018)" role="img" aria-label="Model crouching among foliage"></div>
<div class="abs gram photo" style="left:354px;top:4195px;background:linear-gradient(180deg,#c98a4e,#3a2a22)" role="img" aria-label="Hoodie back print in warm light"></div>
<div class="abs gram photo" style="left:608px;top:4195px;background:linear-gradient(180deg,#d5dde2,#6e7a6a)" role="img" aria-label="Two models in white and black tees"></div>
<div class="abs gram photo" style="left:862px;top:4195px;background:linear-gradient(180deg,#5c7b3e,#d8ddd2)" role="img" aria-label="Model in a white tee outdoors"></div>

<div class="abs perk" style="left:101px"><span class="perk-icon"><svg width="22" height="22" viewBox="0 0 24 24" fill="none" stroke="#444" stroke-width="1.6"><path d="M5 3h4l2 5-3 2a12 12 0 006 6l2-3 5 2v4a2 2 0 01-2 2A18 18 0 013 5a2 2 0 012-2z"/></svg></span><div><h4>Customer Support</h4><p>Mon - Sat, 10am - 9pm</p></div></div>
<div class="abs perk" style="left:360px"><span class="perk-icon"><svg width="22" height="22" viewBox="0 0 24 24" fill="none" stroke="#444" stroke-width="1.6"><path d="M3 7l9-4 9 4v10l-9 4-9-4z"/><path d="M3 7l9 4 9-4M12 11v10"/></svg></span><div><h4>Easy Returns</h4><p>Returns extended to 60 days</p></div></div>
<div class="abs perk" style="left:643px"><span class="perk-icon"><svg width="22" height="22" viewBox="0 0 24 24" fill="none" stroke="#444" stroke-width="1.6"><rect x="3" y="9" width="18" height="12"/><path d="M2 9h20M12 9v12M12 9c-2-5-7-5-6-1M12 9c2-5 7-5 6-1"/></svg></span><div><h4>Gift Package</h4><p>Free packaging over $100</p></div></div>
<div class="abs perk" style="left:912px"><span class="perk-icon"><svg width="22" height="22" viewBox="0 0 24 24" fill="none" stroke="#444" stroke-width="1.6"><circle cx="12" cy="9" r="6"/><path d="M8 14l-2 8 6-3 6 3-2-8"/></svg></span><div><h4>One-year Warranty</h4><p>No questions asked</p></div></div>

<footer class="abs site-footer"></footer>
<div class="abs foot-head" style="left:101px">SIGN FOR NEWSLETTER</div>
<div class="abs newsletter">Enter your email</div>
<svg class="abs" style="left:293px;top:4720px" width="14" height="14" viewBox="0 0 14 14" fill="#fff"><path d="M1 7l12-6-4 12-2-5z"/></svg>
<span class="abs social" style="left:101px"></span>
<span class="abs social" style="left:146px"></span>
<span class="abs social" style="left:192px"></span>
<span class="abs social" style="left:237px"></span>

<div class="abs foot-head" style="left:420px">CUSTOMER SERVICE</div>
<ul class="abs foot-list" style="left:420px"><li>Shipping</li><li>Special Deals</li><li>Start A Return</li><li>Return Policy</li><li>Dealer Inquiries</li><li>Contact Us</li><li>Privacy Policy</li></ul>
<div class="abs foot-head" style="left:681px">RESOURCES</div>
<ul class="abs foot-list" style="left:681px"><li>Account Log In</li><li>Blog</li><li>Gift Cards</li><li>Brand Kit</li><li>Affiliate Program</li><li>Terms Of Service</li></ul>

<div class="abs foot-brand"><span class="foot-brand-dot"></span>Tidalux Globalwear Co.</div>
<div class="abs store-link"><svg width="10" height="13" viewBox="0 0 10 13" fill="#fff"><path d="M5 0a5 5 0 00-5 5c0 4 5 8 5 8s5-4 5-8a5 5 0 00-5-5zm0 7a2 2 0 110-4 2 2 0 010 4z"/></svg>FIND A RETAIL STORE</div>
<span class="abs pay" style="left:892px;background:#e9edf3"></span>
<span class="abs pay" style="left:943px;background:#e9803a"></span>
<span class="abs pay" style="left:993px;background:#2b3f8f"></span>
<span class="abs pay" style="left:1045px;background:#3a8fd6"></span>

<div class="abs copyright">©Copyright ©2023 Tidalux Globalwear Co. All Rights Reserved.</div>

</body>
</html>
```